Label for LiPo Battery Product for RC Hobby Industry

We need your creativity for a new lithium battery label design. We aim to make our product visually appealing and distinct from competitors. Your design skills are crucial for this task, and we're excited to work with you.
Our main label feature is the colour tag profile, designed to easily identify battery category and power level with a 2-way colour band. Inspired by a tool company that uses a consistent colour profile to identify Phillips head sizing across their range.
The design should be modern, clear, convey speed and suitable for both professional and consumer markets.
Target Market(s)
RC, Drone, Camera community. 20-30 year old.
Industry/Entity Type
Battery, Drone Industry, RC Car
Requirements
Must have
- 2-Way colour tag identity profiling, clear text at 100% scale
Nice to have
- Text and graphic alignment. Comfortable padding and formatting. Colour tag profile, clear text."
Should not have
- Basic, stock looking image.

```html
<!DOCTYPE html>
<html lang="en">
<head>
<meta charset="utf-8">
<title>TX130 LiPo Battery Label</title>
<link rel="stylesheet" href="https://fonts.googleapis.com/css2?family=Russo+One&family=Oswald:wght@600&family=Audiowide&display=swap">
<style>
  :root {
    --ink: #050505;
    --paper: #ffffff;
    --red: #b82036;
    --teal: #1fa3b2;
    --charcoal: #242424;
  }
  html, body {
    margin: 0;
    padding: 0;
    width: 713px;
    height: 1200px;
    overflow: hidden;
    background: var(--paper);
  }
  .canvas {
    position: relative;
    width: 713px;
    height: 1200px;
  }
  .label {
    position: absolute;
    left: 73px;
    top: 126px;
    width: 567px;
    height: 312px;
    background: var(--paper);
    overflow: hidden;
    outline: 1px solid #eeeeee;
  }
  .label__field {
    position: absolute;
    left: 0;
    top: 11px;
    width: 420px;
    height: 290px;
    background: var(--ink);
  }
  .label__texture {
    position: absolute;
    left: 380px;
    top: 11px;
    width: 150px;
    height: 290px;
    background: linear-gradient(90deg, var(--ink) 0%, #2a2a2a 35%, #bdbdbd 75%, var(--paper) 100%);
  }
  .model {
    position: absolute;
    left: 24px;
    top: 26px;
    margin: 0;
    font-family: "Russo One", sans-serif;
    font-size: 72px;
    line-height: 1;
    letter-spacing: 1px;
    transform-origin: left top;
    transform: skewX(-12deg) scaleX(1.2);
    color: var(--paper);
  }
  .tag-stripe {
    position: absolute;
    height: 10px;
    transform: skewX(-20deg);
  }
  .tag-stripe--teal { left: 20px; top: 108px; width: 221px; background: var(--teal); }
  .tag-stripe--red { left: 13px; top: 122px; width: 228px; background: var(--red); }
  .capacity-short {
    position: absolute;
    left: 243px;
    top: 100px;
    font-family: "Oswald", sans-serif;
    font-weight: 600;
    font-size: 38px;
    line-height: 1;
    letter-spacing: -1px;
    color: var(--paper);
  }
  .spec {
    position: absolute;
    top: 162px;
    width: 75px;
    height: 30px;
    background: var(--red);
    display: flex;
    align-items: center;
    justify-content: center;
    font-family: "Russo One", sans-serif;
    font-size: 12px;
    font-style: italic;
    color: var(--ink);
  }
  .spec--rate { left: 45px; }
  .spec--cells { left: 142px; }
  .spec--voltage { left: 240px; }
  .capacity {
    position: absolute;
    left: 80px;
    top: 216px;
    font-family: "Russo One", sans-serif;
    font-size: 30px;
    line-height: 1;
    transform-origin: left top;
    transform: skewX(-10deg) scaleX(1.42);
    color: var(--paper);
  }
  .feature-band {
    position: absolute;
    left: 0;
    top: 272px;
    width: 425px;
    height: 30px;
    background: var(--teal);
    display: flex;
    align-items: center;
    padding-left: 8px;
    box-sizing: border-box;
    font-family: "Russo One", sans-serif;
    font-size: 10.5px;
    font-style: italic;
    letter-spacing: 0.2px;
    color: var(--ink);
    white-space: nowrap;
  }
  .power-band {
    position: absolute;
    left: 0;
    top: 301px;
    width: 438px;
    height: 11px;
    background: var(--red);
  }
  .brand {
    position: absolute;
    left: 492px;
    top: 26px;
    writing-mode: vertical-rl;
    font-family: "Audiowide", sans-serif;
    font-size: 50px;
    line-height: 1;
    letter-spacing: 2px;
    color: var(--charcoal);
  }
  .brand-run {
    position: absolute;
    left: 548px;
    top: 6px;
    writing-mode: vertical-rl;
    font-family: "Russo One", sans-serif;
    font-size: 6px;
    line-height: 1;
    color: var(--charcoal);
    white-space: nowrap;
  }
</style>
</head>
<body>
<main class="canvas">
  <section class="label">
    <div class="label__field"></div>
    <div class="label__texture" role="img" aria-label="Grunge paint splatter texture fading from black into white"></div>

    <h1 class="model">TX130</h1>
    <div class="tag-stripe tag-stripe--teal"></div>
    <div class="tag-stripe tag-stripe--red"></div>
    <div class="capacity-short">1.3Ah</div>

    <div class="spec spec--rate">120C</div>
    <div class="spec spec--cells">6 CELLS</div>
    <div class="spec spec--voltage">22.2V</div>

    <div class="capacity">1300MAH</div>

    <div class="feature-band">PERFORMANCE • ARMOR PROTECTION • ADVANCED INSULATION</div>
    <div class="power-band"></div>

    <div class="brand">KORVAN</div>
    <div class="brand-run">KORVAN KORVAN KORVAN KORVAN KORVAN KORVAN KORVAN KORVAN KORVAN</div>
  </section>
</main>
</body>
</html>
```